The Book Cover for "Finding the Silver Lantern of Dawn" needs redesigned

First the back ground or art work needs to be replaced or redesigned.
The title Finding the Silver Lantern of Dawn needs to be redesigned so that the words "Finding the" is diminished in size compared to the rest of the title "Silver Lantern of Dawn"
The Sub-title "Tracing the forgotten path of the Evening Wind" needs to be more pronounced and readable.
The authors name needs to be downsized.

```html
<!DOCTYPE html>
<html lang="en">
<head>
<meta charset="UTF-8">
<title>Finding the Silver Lantern of Dawn — Book Cover</title>
<link href="https://fonts.googleapis.com/css2?family=Gloock&family=Fjalla+One&display=swap" rel="stylesheet">
<style>
  :root {
    --page-bg: #eee6ec;
    --band: #c57bb2;
    --band-text: #ffffff;
    --title: #6a2152;
    --sky-top: #f6e6f3;
    --sky-mid: #ecc6e1;
    --trees: #a8508f;
    --ground: #8f3f7c;
    --author: #fbeef7;
  }
  * { margin: 0; padding: 0; box-sizing: border-box; }
  html, body {
    width: 1200px;
    height: 768px;
    overflow: hidden;
    background: var(--page-bg);
  }
  .canvas {
    position: relative;
    width: 1200px;
    height: 768px;
  }
  .book-cover {
    position: absolute;
    left: 363px;
    top: 24px;
    width: 473px;
    height: 720px;
    overflow: hidden;
    box-shadow: 0 10px 30px rgba(90, 30, 70, 0.25);
  }
  .cover-art {
    position: absolute;
    inset: 0;
    background:
      radial-gradient(circle at 22% 47%, rgba(255,255,255,0.95) 0, rgba(255,255,255,0.55) 60px, rgba(255,255,255,0) 150px),
      linear-gradient(180deg, var(--sky-top) 0%, var(--sky-mid) 45%, var(--trees) 62%, #b865a2 80%, var(--ground) 100%);
  }
  .subtitle-band {
    position: absolute;
    left: 0; right: 0; top: 0;
    height: 33px;
    background: var(--band);
    display: flex;
    align-items: center;
    justify-content: center;
  }
  .subtitle {
    font-family: "Fjalla One", sans-serif;
    font-size: 17px;
    letter-spacing: 0.6px;
    color: var(--band-text);
    white-space: nowrap;
  }
  .title {
    position: absolute;
    right: 30px;
    top: 62px;
    text-align: right;
    font-family: "Gloock", serif;
    color: var(--title);
    font-weight: 400;
  }
  .title-lead {
    display: block;
    font-size: 33px;
    line-height: 1.1;
    margin-bottom: 2px;
  }
  .title-main {
    display: block;
    font-size: 68px;
    line-height: 0.98;
  }
  .title-final {
    display: flex;
    justify-content: flex-end;
    align-items: center;
    gap: 8px;
  }
  .title-small {
    font-size: 30px;
    line-height: 1;
    align-self: flex-start;
    margin-top: 6px;
  }
  .author {
    position: absolute;
    right: 30px;
    bottom: 24px;
    font-family: "Fjalla One", sans-serif;
    font-size: 15px;
    letter-spacing: 0.4px;
    color: var(--author);
  }
</style>
</head>
<body>
<div class="canvas">
  <section class="book-cover">
    <div class="cover-art" role="img" aria-label="Soft pink-toned photograph of tall misty trees with sunlight glowing through, and a mother standing in a meadow cradling her baby"></div>

    <header class="subtitle-band">
      <p class="subtitle">Tracing the forgotten path of the Evening Wind</p>
    </header>

    <h1 class="title">
      <span class="title-lead">Finding the</span>
      <span class="title-main">Silver</span>
      <span class="title-main">Lantern</span>
      <span class="title-main title-final"><span class="title-small">of</span>Dawn</span>
    </h1>

    <p class="author">R T Lane Ashworth</p>
  </section>
</div>
</body>
</html>
```